Report Cover and Format For Company

Hello, I would like a report cover for my company and document format that will be used for reports, proposals and documents to customers.

Industry/Entity Type

Information Technology

```html
<!DOCTYPE html>
<html lang="en">
<head>
<meta charset="utf-8">
<title>Northgate Systems — Stationery Set</title>
<link href="https://fonts.googleapis.com/css2?family=PT+Sans:ital,wght@0,400;0,700;1,400;1,700&display=swap" rel="stylesheet">
<style>
  :root {
    --stage: #e8e8e8;
    --ink: #0b0b0b;
    --paper: #e3e3e3;
    --cyan: #19b5dc;
    --blue: #1a7db4;
    --steel: #3a3a3a;
    --white: #ffffff;
    --muted: #d8d8d8;
  }
  * { box-sizing: border-box; margin: 0; padding: 0; }
  html, body {
    width: 1200px; height: 800px; overflow: hidden;
    background: var(--stage);
    font-family: "PT Sans", Arial, sans-serif;
  }
  .canvas { position: relative; width: 1200px; height: 800px; }

  /* Brand name lockup (stands in for the mark) */
  .brand { display: flex; align-items: center; gap: 8px; color: var(--blue); font-weight: 700; text-transform: uppercase; line-height: 1; }
  .brand-square { background: var(--blue); flex: none; }
  .brand-name { display: flex; flex-direction: column; }

  /* Business cards */
  .card { position: absolute; top: 50px; width: 340px; height: 196px; background: var(--paper); overflow: hidden; }
  .card--front { left: 240px; display: flex; }
  .card--back { left: 630px; display: flex; flex-direction: column; align-items: center; justify-content: center; gap: 22px; }
  .card-brand-side { width: 50%; display: flex; align-items: center; justify-content: center; }
  .card-brand-side .brand { font-size: 13px; }
  .card-brand-side .brand-square { width: 22px; height: 22px; }
  .card-info-side { width: 50%; background: var(--ink); border-left: 3px solid var(--cyan); padding: 40px 0 0 18px; }
  .card-title { color: var(--white); font-size: 10px; font-weight: 700; text-transform: uppercase; margin-bottom: 10px; }
  .card-title .accent { color: var(--cyan); }
  .contact-list { list-style: none; color: var(--muted); font-size: 8.5px; line-height: 1.25; }
  .contact-list li { display: flex; align-items: flex-start; gap: 7px; margin-bottom: 3px; }
  .contact-list svg { width: 8px; height: 8px; flex: none; margin-top: 1px; fill: var(--cyan); }
  .contact-list .gap { margin-top: 6px; }
  .card--back .brand { font-size: 16px; }
  .card--back .brand-square { width: 28px; height: 28px; }
  .card-web { font-size: 9px; font-weight: 700; color: var(--steel); text-transform: uppercase; }

  /* Report folder spread */
  .folder { position: absolute; left: 150px; top: 300px; width: 900px; height: 460px; background: var(--ink); display: flex; }
  .folder-back, .folder-front { position: relative; width: 50%; height: 100%; }
  .folder-back .brand { position: absolute; left: 26px; bottom: 36px; font-size: 22px; }
  .folder-back .brand-square { width: 40px; height: 40px; }
  .folder-contact { position: absolute; left: 260px; bottom: 36px; text-align: right; font-style: italic; color: var(--muted); font-size: 7px; line-height: 1.45; }
  .folder-contact .card-title { font-size: 7.5px; margin-bottom: 4px; font-style: italic; }
  .folder-contact .contact-list li { justify-content: flex-end; gap: 5px; margin: 0; font-size: 7px; }
  .folder-contact .contact-list svg { width: 6px; height: 6px; order: 2; }
  .folder-front .brand { position: absolute; right: 40px; top: 200px; font-size: 24px; }
  .folder-front .brand-square { width: 44px; height: 44px; }
  .folder-tab { position: absolute; right: 14px; top: 196px; width: 16px; height: 98px; background: var(--cyan); }
  .folder-web { position: absolute; right: 100px; bottom: 24px; color: var(--cyan); font-size: 8.5px; font-weight: 700; font-style: italic; text-transform: uppercase; }
</style>
</head>
<body>
<main class="canvas">

  <section class="card card--front" aria-label="Business card, front">
    <div class="card-brand-side">
      <div class="brand"><span class="brand-square"></span><span class="brand-name"><span>Northgate</span><span>Systems</span></span></div>
    </div>
    <div class="card-info-side">
      <p class="card-title">Northgate <span class="accent">Systems</span></p>
      <ul class="contact-list">
        <li><svg viewBox="0 0 10 10"><path d="M5 0a3.5 3.5 0 0 0-3.5 3.5C1.5 6 5 10 5 10s3.5-4 3.5-6.5A3.5 3.5 0 0 0 5 0zm0 5a1.4 1.4 0 1 1 0-2.8A1.4 1.4 0 0 1 5 5z"/></svg><span>18 Alder Crest Way<br>Brookfield, 06804</span></li>
        <li class="gap"><svg viewBox="0 0 10 10"><path d="M2 0.5l2 2-1 1.2a6 6 0 0 0 3.3 3.3l1.2-1 2 2-1.3 1.5C4.5 9.5 0.5 5.5 0.5 2z"/></svg><span>555-210-4830</span></li>
        <li><svg viewBox="0 0 10 10"><path d="M5 0a5 5 0 1 0 0 10A5 5 0 0 0 5 0zm0 1.2c.6.7 1.1 1.9 1.2 3.2H3.8C3.9 3.1 4.4 1.9 5 1.2zM3.8 5.6h2.4c-.1 1.3-.6 2.5-1.2 3.2-.6-.7-1.1-1.9-1.2-3.2z"/></svg><span>www.northgatesystems.com</span></li>
        <li><svg viewBox="0 0 10 10"><path d="M0 2h10v6H0zm1 1v.3l4 2.4 4-2.4V3z"/></svg><span>hello@northgatesystems.com</span></li>
      </ul>
    </div>
  </section>

  <section class="card card--back" aria-label="Business card, back">
    <div class="brand"><span class="brand-square"></span><span class="brand-name"><span>Northgate</span><span>Systems</span></span></div>
    <p class="card-web">www.northgatesystems.com</p>
  </section>

  <section class="folder" aria-label="Report cover spread">
    <div class="folder-back">
      <div class="brand"><span class="brand-square"></span><span class="brand-name"><span>Northgate</span><span>Systems</span></span></div>
      <div class="folder-contact">
        <p class="card-title">Northgate <span class="accent" style="color:var(--cyan)">Systems</span></p>
        <ul class="contact-list">
          <li><svg viewBox="0 0 10 10"><path d="M5 0a3.5 3.5 0 0 0-3.5 3.5C1.5 6 5 10 5 10s3.5-4 3.5-6.5A3.5 3.5 0 0 0 5 0zm0 5a1.4 1.4 0 1 1 0-2.8A1.4 1.4 0 0 1 5 5z"/></svg><span>18 Alder Crest Way<br>Brookfield, 06804</span></li>
          <li><svg viewBox="0 0 10 10"><path d="M2 0.5l2 2-1 1.2a6 6 0 0 0 3.3 3.3l1.2-1 2 2-1.3 1.5C4.5 9.5 0.5 5.5 0.5 2z"/></svg><span>555-210-4830</span></li>
          <li><svg viewBox="0 0 10 10"><path d="M5 0a5 5 0 1 0 0 10A5 5 0 0 0 5 0zm0 1.2c.6.7 1.1 1.9 1.2 3.2H3.8C3.9 3.1 4.4 1.9 5 1.2zM3.8 5.6h2.4c-.1 1.3-.6 2.5-1.2 3.2-.6-.7-1.1-1.9-1.2-3.2z"/></svg><span>www.northgatesystems.com</span></li>
          <li><svg viewBox="0 0 10 10"><path d="M0 2h10v6H0zm1 1v.3l4 2.4 4-2.4V3z"/></svg><span>hello@northgatesystems.com</span></li>
        </ul>
      </div>
    </div>
    <div class="folder-front">
      <div class="brand"><span class="brand-square"></span><span class="brand-name"><span>Northgate</span><span>Systems</span></span></div>
      <span class="folder-tab"></span>
      <p class="folder-web">www.northgatesystems.com</p>
    </div>
  </section>

</main>
</body>
</html>
```